Nazareth city only beer brewer needs bottle label and logo improvement.

we are starting a small brewery located in Nazareth Town, Israel.
we want a label design to match a Beer bottle which will have several types like, Ale, Wheat, Dark, Amber, so I will need the psd to be able to change between those. we're located in Nazareth the old biblical city, we don't want christian signs in our label but we want Hadley's well somehow embedded in a creative way inside the Logo.

Nazareth is an old historical city, so I want the label to resemble that design somehow. I want the label to wrap the bottle.

Thank you

Target Market(s)

Bars, Alcohol Stores, Beer Festivals, Beer Drinkers.

Industry/Entity Type

Brewery

Logo Text

Olvenmark Beer

Font styles to use
Decorative

Requirements
Must have
• standard size of label for 330 ml bottle..
• on the front:
• 1. we already have a logo which we want to improve or refactor in an artistic way if it's possible, if not we can give it up if there's better Ideas to embed Hadley's well sculpture (google Hadley's well to see more). I'm going to add money for Logo refactoring and will attach the original logo. hops and barley plants embedded in the design creatively.
• be careful to use photos because of reserved copyrights.
• 2. alcohol percentage, Beer type (dark, light, lager, Amber, weiss... and so on), bottle size (330ml for example). please remember i will need the psd file for the label because we are creating different types of beers.
• on the back:
• 1. to have like a little story which we can edit, a little info about an old building in the city, or an interesting historical event or character.
• 2. ingredients line. (Ingredients: Water, Malt, Beer Yeast, Hops, ..)
• 3. nutrition value: 50 Calories per 100 ml
• 4. "learn more about us at www.olvenmarkbeer-brew.net"
• 5. production date little box.
• 6. "Handcrafted By Olvenmark Brewery"
• 7. " this product is fresh and not pasteurized. use it before up to 6 months from production date"
• 8. bottle size and alcohol meter.
• 9. warning! drinking alcohol and driving increases the risk of injury or death. (should be in a white box)
• 10. please recycle for cleaner environment. 30 Agorot Deposit
• 11. about the colors. be creative. attract the eye, not many colors.
• 12. a box for barcode.
Nice to have
• (big advantage) we want the Palestinian embroidery somehow smoothly embedded or decorating the label. (not too noisy and bold)
Should not have
• too many colors.

```html
<!DOCTYPE html>
<html lang="en">
<head>
<meta charset="utf-8">
<title>Amber Beer Label</title>
<link rel="stylesheet" href="https://fonts.googleapis.com/css2?family=Cinzel+Decorative:wght@400&family=Crimson+Text:wght@400;600&display=swap">
<style>
  :root {
    --backdrop: #efeadf;
    --label-red: #7c1014;
    --label-deep: #4e0609;
    --label-ink: #2e0305;
    --copper: #e0774a;
    --copper-light: #f3a479;
    --wheat-tone: #b8452c;
  }
  html, body {
    margin: 0;
    padding: 0;
    width: 1094px;
    height: 1200px;
    overflow: hidden;
    background: var(--backdrop);
  }
  .canvas {
    position: relative;
    width: 1094px;
    height: 1200px;
  }
  .label {
    position: absolute;
    left: 157px;
    top: 80px;
    width: 780px;
    height: 1040px;
    background: var(--label-red);
    box-shadow: 0 10px 30px rgba(60, 10, 10, 0.18);
    overflow: hidden;
  }
  .label-art {
    position: absolute;
    inset: 0;
  }
  .abv {
    position: absolute;
    top: 8px;
    left: 0;
    width: 100%;
    text-align: center;
    font-family: "Crimson Text", serif;
    font-weight: 600;
    font-size: 30px;
    color: var(--copper-light);
    letter-spacing: 0.5px;
  }
  .beer-type {
    position: absolute;
    top: 540px;
    left: 0;
    width: 100%;
    text-align: center;
    font-family: "Cinzel Decorative", serif;
    font-size: 132px;
    line-height: 1;
    color: var(--copper);
  }
  .volume {
    position: absolute;
    top: 712px;
    left: 0;
    width: 100%;
    text-align: center;
    font-family: "Crimson Text", serif;
    font-size: 30px;
    color: var(--copper-light);
  }
</style>
</head>
<body>
<div class="canvas">
  <div class="label">
    <svg class="label-art" width="780" height="1040" viewBox="0 0 780 1040">
      <defs>
        <linearGradient id="wheatField" x1="0" y1="0" x2="1" y2="0">
          <stop offset="0" stop-color="#6a0c10"/>
          <stop offset="0.5" stop-color="#8a1a16"/>
          <stop offset="1" stop-color="#6a0c10"/>
        </linearGradient>
        <linearGradient id="wellTone" x1="0" y1="0" x2="0" y2="1">
          <stop offset="0" stop-color="#f09a6a"/>
          <stop offset="1" stop-color="#c9603a"/>
        </linearGradient>
      </defs>

      <!-- top band -->
      <rect class="top-band" x="0" y="0" width="780" height="54" fill="var(--label-deep)"/>
      <line x1="0" y1="54" x2="780" y2="54" stroke="var(--copper)" stroke-width="3"/>

      <!-- barley pattern field -->
      <rect class="barley-field" x="0" y="57" width="780" height="893" fill="url(#wheatField)"
            role="img" aria-label="Vertical rows of stylised barley ears pattern"/>

      <!-- bottom band -->
      <rect class="bottom-band" x="0" y="950" width="780" height="90" fill="var(--label-deep)"/>
      <line x1="0" y1="950" x2="780" y2="950" stroke="var(--copper)" stroke-width="3"/>
      <line x1="0" y1="972" x2="780" y2="972" stroke="var(--label-ink)" stroke-width="6"/>

      <!-- ribbon wings -->
      <path class="ribbon" d="M0,300 L780,300 L780,360 L0,360 Z" fill="var(--copper)" opacity="0.85"/>
      <path class="ribbon-shade" d="M0,360 L780,360 L780,372 L0,372 Z" fill="var(--label-ink)" opacity="0.5"/>
      <path class="ribbon" d="M0,760 L780,760 L780,810 L0,810 Z" fill="var(--copper)" opacity="0.55"/>

      <!-- cartouche -->
      <path class="cartouche-frame"
            d="M80,290 Q390,210 700,290 L700,690 Q700,735 655,752 L430,832 Q390,846 350,832 L125,752 Q80,735 80,690 Z"
            fill="var(--copper)"/>
      <path class="cartouche-inner"
            d="M104,306 Q390,236 676,306 L676,684 Q676,718 642,732 L424,808 Q390,820 356,808 L138,732 Q104,718 104,684 Z"
            fill="var(--label-deep)"/>
      <path d="M120,320 Q390,256 660,320 L660,678 Q660,706 632,718 L420,792 Q390,802 360,792 L148,718 Q120,706 120,678 Z"
            fill="none" stroke="var(--copper)" stroke-width="2" opacity="0.7"/>

      <!-- well emblem area -->
      <rect class="well-emblem" x="190" y="270" width="400" height="200" rx="6" fill="url(#wellTone)"
            role="img" aria-label="Illustration of the stone well building with arched roof"/>

      <!-- divider under emblem -->
      <line x1="170" y1="500" x2="610" y2="500" stroke="var(--copper)" stroke-width="2" opacity="0.6"/>
    </svg>

    <div class="abv">Alc 4,8% Vol.</div>
    <div class="beer-type">Amber</div>
    <div class="volume">0.33 ml</div>
  </div>
</div>
</body>
</html>
```